K7 Morvane Advisory Partners Ltd - Website Design

We already have a company logo. We need a website created for our consulting agency.
Refer to attached files for logo and website content.
We would also be open to any additional recommendations.
Industry/Entity Type
Finance And Accounting
Coding
Coded - Design and coding required
Number of Pages Required
1 page
Font styles to use
Serif
Colors
3377b5
b868aa
33b8a4
Requirements
Must have
- Company Logo, name and who we are.

```html
<!DOCTYPE html>
<html lang="en">
<head>
<meta charset="utf-8">
<title>K7 Morvane Advisory Partners Ltd</title>
<link href="https://fonts.googleapis.com/css2?family=Fira+Sans:wght@400;500;600;700&family=Roboto:ital,wght@0,400;0,500;0,700;1,400&display=swap" rel="stylesheet">
<style>
:root{
  --blue:#3377b5;
  --purple:#b868aa;
  --teal:#33b8a4;
  --navy:#0c1628;
  --ink:#151a22;
  --muted:#8a909a;
  --pale:#eef4fa;
  --line:#dde3ea;
  --white:#ffffff;
}
*{box-sizing:border-box;margin:0;padding:0}
html,body{width:1200px;height:4471px;overflow:hidden}
body{position:relative;font-family:'Roboto',sans-serif;color:var(--ink);background:var(--white)}
.abs{position:absolute}
h1,h2,h3{font-family:'Fira Sans',sans-serif}
.section-title{position:absolute;left:0;width:1200px;text-align:center;font-size:44px;font-weight:600;color:var(--ink)}
.btn{position:absolute;display:flex;align-items:center;justify-content:center;font-size:15px;font-weight:700;letter-spacing:.3px;color:var(--white);background:var(--purple)}
.stripe{position:absolute;left:0;top:0}

/* hero */
.hero{position:absolute;left:0;top:0;width:1200px;height:592px;background:linear-gradient(100deg,#050b16 0%,#0c1a2e 45%,#1a3550 70%,#0a1424 100%);overflow:hidden}
.hero-visual{position:absolute;left:500px;top:80px;width:620px;height:500px;background:radial-gradient(ellipse at 55% 55%,rgba(90,150,200,.45),rgba(20,45,75,.2) 55%,transparent 75%)}
.brand{position:absolute;display:flex;align-items:center;gap:10px;color:var(--white);font-family:'Fira Sans',sans-serif;font-weight:500}
.brand .mark{width:18px;height:18px;border-radius:50%;border:2px solid var(--white)}
.nav{position:absolute;top:48px;font-size:14px;color:var(--white);font-weight:500}
.hero-title{position:absolute;left:99px;top:205px;font-size:58px;font-weight:700;color:var(--white)}
.hero-text{position:absolute;left:99px;top:288px;width:395px;font-size:13.5px;line-height:26px;color:var(--white);font-weight:500}
.dots{position:absolute;top:555px;left:512px;display:flex;gap:8px}
.dots span{width:38px;height:3px;background:rgba(255,255,255,.35)}
.dots span.on{background:var(--teal)}

/* who */
.who-photo{position:absolute;left:144px;top:703px;width:483px;height:353px;background:linear-gradient(135deg,#aab8c6,#dfe6ec 45%,#7f93a6)}
.eyebrow{position:absolute;font-size:15px;color:var(--teal);font-weight:500}
.who-title{position:absolute;left:686px;top:752px;font-size:45px;font-weight:600}
.body-text{font-size:13.5px;line-height:24.5px;color:#555c66}

/* offer */
.offer{position:absolute;left:0;top:1162px;width:1200px;height:714px;background:var(--pale);overflow:hidden}
.grid{position:absolute;left:160px;top:191px;width:879px;height:436px;display:grid;grid-template-columns:repeat(3,1fr);grid-template-rows:repeat(2,1fr);border:1px solid var(--line)}
.cell{border-right:1px solid var(--line);border-bottom:1px solid var(--line);text-align:center;padding-top:30px}
.cell:nth-child(3n){border-right:none}
.cell:nth-child(n+4){border-bottom:none}
.cell.active{background:var(--white);box-shadow:0 4px 18px rgba(0,0,0,.08)}
.cell svg{width:56px;height:56px}
.cell h3{font-size:18px;font-weight:500;margin-top:12px;margin-bottom:6px}
.cell p{font-size:12.5px;line-height:21px;color:var(--muted);padding:0 18px}

/* reviews */
.review{position:absolute;top:2050px;width:464px;height:260px;background:var(--white);box-shadow:0 2px 16px rgba(0,0,0,.08);padding:28px 28px}
.review p{font-size:16.5px;line-height:27px;font-style:italic;color:#2a2f36}
.author{position:absolute;left:28px;bottom:16px;right:28px;display:flex;align-items:center;gap:12px;font-size:16px;font-weight:500}
.avatar{width:36px;height:36px;border-radius:50%;background:#c7ced6}
.stars{margin-left:auto;color:#f2b821;font-size:20px;letter-spacing:1px}
.arrow{position:absolute;top:2159px;width:42px;height:42px;border-radius:50%;background:var(--white);box-shadow:0 1px 8px rgba(0,0,0,.12);display:flex;align-items:center;justify-content:center}

/* cta */
.cta{position:absolute;left:0;top:2423px;width:1200px;height:341px;background:linear-gradient(90deg,#2f6eaa,#3a7dbd 50%,#3271ad);overflow:hidden}

/* blogs */
.blog-img{position:absolute;top:2939px;width:318px;height:236px}
.blog-card{position:absolute;top:3137px;width:288px;height:215px;background:var(--white);box-shadow:0 3px 14px rgba(0,0,0,.1);padding:20px 18px}
.blog-date{display:flex;align-items:center;gap:8px;font-size:12.5px;color:#333}
.blog-card h3{font-family:'Roboto',sans-serif;font-size:16.5px;font-weight:700;line-height:25px;margin:10px 0 8px}
.blog-card p{font-size:12.5px;line-height:21px;color:var(--muted)}
.read{font-size:13px;color:var(--purple);font-weight:700;margin-top:12px}

/* partners */
.tabs{position:absolute;top:3514px;left:0;width:1200px;display:flex;justify-content:center;gap:22px;font-size:17px}
.tabs .on{border-bottom:2px solid var(--blue);padding-bottom:4px;color:var(--ink)}
.tabs .off{color:var(--muted)}
.partner{position:absolute;top:3588px;display:flex;align-items:center;gap:8px;font-family:'Fira Sans',sans-serif;font-size:30px;font-weight:600;color:#6f747b}
.partner i{display:block;width:22px;height:22px;border-radius:50%;background:#8c9198}

/* contact */
.contact{position:absolute;left:0;top:3703px;width:1200px;height:563px;background:linear-gradient(160deg,#2c5f99,#3a78b8 55%,#2a5a92);overflow:hidden}
.contact-row{position:absolute;left:247px;display:flex;align-items:flex-start;gap:12px;color:var(--white);font-size:14.5px;line-height:20px}
.ico{width:26px;height:26px;border-radius:50%;background:var(--purple);flex:none;display:flex;align-items:center;justify-content:center}
.social{position:absolute;top:4153px;width:34px;height:34px;border-radius:50%;background:var(--white)}
.form{position:absolute;left:613px;top:3790px;width:342px;height:396px;background:var(--navy);border-radius:12px;overflow:hidden}
.form-head{height:60px;background:var(--teal);color:var(--white);font-family:'Fira Sans',sans-serif;font-size:20px;font-weight:500;padding:18px 30px}
.field{position:absolute;left:30px;width:282px;border-bottom:1px solid #7d8796;color:var(--white);font-size:14px;padding-bottom:12px}

/* footer */
.footer{position:absolute;left:0;top:4266px;width:1200px;height:205px;background:#0b1424}
.foot-link{position:absolute;top:80px;color:var(--white);font-size:15px;font-weight:700}
</style>
</head>
<body>

<!-- HERO -->
<section class="hero">
  <div class="hero-visual" role="img" aria-label="Photo of an open hand beneath glowing hexagonal finance data icons"></div>
  <svg class="stripe" width="1200" height="592" viewBox="0 0 1200 592">
    <polygon points="78,0 130,0 0,130 0,78" fill="#33b8a4"/>
    <polygon points="1200,417 1200,503 1130,592 1042,592" fill="#33b8a4"/>
  </svg>
  <div class="brand" style="left:109px;top:40px;font-size:26px"><span class="mark"></span>K7 Morvane</div>
  <nav>
    <span class="nav" style="left:483px">Home</span>
    <span class="nav" style="left:571px">About Us</span>
    <span class="nav" style="left:681px">Services</span>
    <span class="nav" style="left:783px">Blog</span>
    <span class="nav" style="left:858px">Contact Us</span>
    <span class="nav" style="left:962px;display:flex;align-items:center;gap:8px">
      <svg width="18" height="18" viewBox="0 0 24 24"><path d="M6 3l3 0 2 5-2 1.5a12 12 0 0 0 5.5 5.5L16 13l5 2v3a2 2 0 0 1-2 2A16 16 0 0 1 4 5a2 2 0 0 1 2-2z" fill="none" stroke="#fff" stroke-width="1.6"/></svg>(555) 014-2290</span>
  </nav>
  <h1 class="hero-title">K7 Morvane</h1>
  <p class="hero-text">Lorem ipsum dolor sit amet, consectetur adipiscing elit, sed do eiusmod tempor incididunt ut labore et dolore magna aliqua. Quis ipsum suspendisse ultrices gravida.</p>
  <div class="btn" style="left:99px;top:387px;width:163px;height:47px">GET STARTED</div>
  <div class="dots"><span></span><span></span><span class="on"></span><span></span></div>
</section>

<!-- WHO WE ARE -->
<div class="who-photo" role="img" aria-label="Photo of an analyst working at a desk with charts on laptop and monitor in a city office"></div>
<div class="eyebrow" style="left:686px;top:726px">WELCOME TO K7 MORVANE</div>
<div class="abs" style="left:905px;top:736px;width:167px;height:1px;background:#c9ced4"></div>
<h2 class="who-title">Who We Are</h2>
<p class="abs body-text" style="left:686px;top:813px;width:420px">Lorem ipsum dolor sit amet, coelit, sed do eiusmod or incididunt ut labore et dolore magna aliqua. Quis ij susisse ultrices gravida. Risus commodo viverra maecenas asan lacus vel facilisis. Lorem ipsum dolor sit amet, coelit, sed do eiod tmr incididunt ut labore et dolore magna aliqua. Quis ij suspensse ultrices gravida. Risus commodo viverra maecenas accumsan lacus vel facilisis.</p>
<div class="btn" style="left:688px;top:981px;width:161px;height:47px">LEARN MORE</div>

<!-- WHAT WE OFFER -->
<section class="offer">
  <svg class="stripe" width="1200" height="714" viewBox="0 0 1200 714">
    <polygon points="78,0 130,0 0,175 0,105" fill="#33b8a4"/>
    <polygon points="1200,540 1200,610 1123,714 1037,714" fill="#33b8a4"/>
  </svg>
  <h2 class="section-title" style="top:104px">What We Offer</h2>
  <div class="grid">
    <div class="cell">
      <svg viewBox="0 0 56 56" fill="none" stroke="#3377b5" stroke-width="1.8"><rect x="8" y="6" width="30" height="40" rx="2"/><rect x="13" y="11" width="20" height="8"/><rect x="26" y="26" width="24" height="24" rx="2" stroke="#33b8a4"/><line x1="30" y1="34" x2="46" y2="34" stroke="#33b8a4"/><line x1="30" y1="42" x2="46" y2="42" stroke="#33b8a4"/></svg>
      <h3>Accounting</h3>
      <p>Lorem ipsum dolor sit amet, ctetur adiscing elit, sed do eiusmod tempor inciunt ut labore et dolore magna aliqua.</p>
    </div>
    <div class="cell">
      <svg viewBox="0 0 56 56" fill="none" stroke="#3377b5" stroke-width="1.8"><rect x="12" y="4" width="32" height="46" rx="2"/><line x1="18" y1="14" x2="38" y2="14"/><line x1="18" y1="22" x2="38" y2="22" stroke="#33b8a4"/><line x1="18" y1="30" x2="38" y2="30"/><line x1="18" y1="38" x2="32" y2="38" stroke="#33b8a4"/></svg>
      <h3>Bookkeeping</h3>
      <p>Lorem ipsum dolor sit amet, ctetur adiscing elit, sed do eiusmod tempor inciunt ut labore et dolore magna aliqua.</p>
    </div>
    <div class="cell">
      <svg viewBox="0 0 56 56" fill="none" stroke="#3377b5" stroke-width="1.8"><rect x="14" y="26" width="6" height="14"/><rect x="24" y="18" width="6" height="22"/><rect x="34" y="10" width="6" height="30"/><polyline points="10,30 22,18 32,14 46,4" stroke="#33b8a4"/><path d="M6 46 h30 l10-6" stroke="#33b8a4"/></svg>
      <h3>Financial Management</h3>
      <p>Lorem ipsum dolor sit amet, ctetur adiscing elit, sed do eiusmod tempor inciunt ut labore et dolore magna aliqua.</p>
    </div>
    <div class="cell">
      <svg viewBox="0 0 56 56" fill="none" stroke="#3377b5" stroke-width="1.8"><polygon points="8,20 26,8 44,20"/><line x1="12" y1="24" x2="12" y2="42"/><line x1="20" y1="24" x2="20" y2="42"/><line x1="32" y1="24" x2="32" y2="42"/><line x1="6" y1="46" x2="46" y2="46"/><rect x="34" y="32" width="18" height="12" rx="2" stroke="#33b8a4"/></svg>
      <h3>Government Grants</h3>
      <p>Lorem ipsum dolor sit amet, ctetur adiscing elit, sed do eiusmod tempor inciunt ut labore et dolore magna aliqua.</p>
    </div>
    <div class="cell active">
      <svg viewBox="0 0 56 56" fill="none" stroke="#3377b5" stroke-width="1.8"><circle cx="28" cy="28" r="16"/><line x1="28" y1="12" x2="28" y2="44" stroke="#33b8a4"/><line x1="12" y1="28" x2="44" y2="28" stroke="#33b8a4"/><rect x="20" y="20" width="6" height="6"/><rect x="30" y="30" width="6" height="6"/></svg>
      <h3>Strategy</h3>
      <p>Lorem ipsum dolor sit amet, ctetur adiscing elit, sed do eiusmod tempor inciunt ut labore et dolore magna aliqua.</p>
    </div>
    <div class="cell">
      <svg viewBox="0 0 56 56" fill="none" stroke="#3377b5" stroke-width="1.8"><circle cx="28" cy="32" r="12" stroke="#33b8a4"/><path d="M8 14 l10 10 M48 14 l-10 10 M28 4 v10"/><polyline points="8,8 8,14 14,14"/><polyline points="48,8 48,14 42,14"/></svg>
      <h3>Mergers and Acquisitions</h3>
      <p>Lorem ipsum dolor sit amet, ctetur adiscing elit, sed do eiusmod tempor inciunt ut labore et dolore magna aliqua.</p>
    </div>
  </div>
</section>

<!-- REVIEWS -->
<h2 class="section-title" style="top:1965px">Client Reviews</h2>
<div class="arrow" style="left:52px"><svg width="16" height="16" viewBox="0 0 16 16"><path d="M14 8H2M7 3L2 8l5 5" fill="none" stroke="#b5bac0" stroke-width="1.5"/></svg></div>
<div class="arrow" style="left:1104px"><svg width="16" height="16" viewBox="0 0 16 16"><path d="M2 8h12M9 3l5 5-5 5" fill="none" stroke="#3377b5" stroke-width="1.5"/></svg></div>
<div class="review" style="left:123px">
  <p>Lorem ipsum dolor sit amet, consectetur adipiscing elit, sed do eiusmod tempor incnt ut labore et dolore magna aliqua. Quis ipsum susdisse ultrices gravida. Risus commodo viverra maecenas accumsan lacus vel facilisis. Lorem ipsum dolor sit amet, consectetur adipiscing elit, sed do eiusmod</p>
  <div class="author"><span class="avatar"></span>Marcus Hale<span class="stars">★★★★★</span></div>
</div>
<div class="review" style="left:611px">
  <p>Lorem ipsum dolor sit amet, consectetur adipiscing elit, sed do eiusmod tempor incnt ut labore et dolore magna aliqua. Quis ipsum susdisse ultrices gravida. Risus commodo viverra maecenas accumsan lacus vel facilisis. Lorem ipsum dolor sit amet, consectetur adipiscing elit, sed do eiusmod</p>
  <div class="author"><span class="avatar"></span>Marcus Hale<span class="stars">★★★★★</span></div>
</div>

<!-- CTA -->
<section class="cta">
  <svg class="stripe" width="1200" height="341" viewBox="0 0 1200 341">
    <polygon points="78,0 130,0 0,175 0,105" fill="#33b8a4"/>
    <polygon points="1200,172 1200,240 1125,341 1040,341" fill="#33b8a4"/>
  </svg>
  <h2 class="section-title" style="top:80px;color:#fff">Get Started Now</h2>
  <svg class="abs" style="left:548px;top:144px" width="104" height="24" viewBox="0 0 104 24"><line x1="0" y1="12" x2="38" y2="12" stroke="#fff" stroke-width="1.5"/><line x1="66" y1="12" x2="104" y2="12" stroke="#fff" stroke-width="1.5"/><circle cx="52" cy="12" r="7" fill="none" stroke="#fff" stroke-width="2"/></svg>
  <div class="btn" style="left:495px;top:201px;width:210px;height:48px;background:#fff;color:var(--blue);font-weight:500">REQUEST FREE DEMO</div>
</section>

<!-- BLOGS -->
<h2 class="section-title" style="top:2848px">Recent Blogs</h2>
<div class="blog-img" style="left:99px;background:linear-gradient(135deg,#8b7a6a,#d8cfc3 50%,#6c7f92)" role="img" aria-label="Photo of two colleagues reviewing work at a desk"></div>
<div class="blog-img" style="left:441px;background:linear-gradient(135deg,#1a1a22,#3b2f2a 45%,#c9703a 75%,#1c1f2a)" role="img" aria-label="Photo of hands over a glowing financial bar chart"></div>
<div class="blog-img" style="left:783px;background:linear-gradient(135deg,#6d7d8c,#b9c2c8 50%,#8a7a68)" role="img" aria-label="Photo of a man reading documents at a table"></div>
<div class="blog-card" style="left:116px">
  <div class="blog-date"><svg width="22" height="18" viewBox="0 0 22 18"><rect x="1" y="2" width="20" height="15" fill="none" stroke="#33b8a4" stroke-width="1.4"/><line x1="1" y1="6" x2="21" y2="6" stroke="#33b8a4" stroke-width="1.4"/></svg>November 14, 2021</div>
  <h3>Lorem ipsum doloet, consectetur adipiscing</h3>
  <p>Lorem ipsum dolor sit amet, consectetur adipiscing elit, sed do eiusmod tempor incididunt ut labore et dolore</p>
  <div class="read">Read More</div>
</div>
<div class="blog-card" style="left:458px">
  <div class="blog-date"><svg width="22" height="18" viewBox="0 0 22 18"><rect x="1" y="2" width="20" height="15" fill="none" stroke="#33b8a4" stroke-width="1.4"/><line x1="1" y1="6" x2="21" y2="6" stroke="#33b8a4" stroke-width="1.4"/></svg>November 14, 2021</div>
  <h3>Lorem ipsum doloet, consectetur adipiscing</h3>
  <p>Lorem ipsum dolor sit amet, consectetur adipiscing elit, sed do eiusmod tempor incididunt ut labore et dolore</p>
  <div class="read">Read More</div>
</div>
<div class="blog-card" style="left:800px">
  <div class="blog-date"><svg width="22" height="18" viewBox="0 0 22 18"><rect x="1" y="2" width="20" height="15" fill="none" stroke="#33b8a4" stroke-width="1.4"/><line x1="1" y1="6" x2="21" y2="6" stroke="#33b8a4" stroke-width="1.4"/></svg>November 14, 2021</div>
  <h3>Lorem ipsum doloet, consectetur adipiscing</h3>
  <p>Lorem ipsum dolor sit amet, consectetur adipiscing elit, sed do eiusmod tempor incididunt ut labore et dolore</p>
  <div class="read">Read More</div>
</div>

<!-- PARTNERS -->
<h2 class="section-title" style="top:3438px;font-size:38px">You’ll be in good company</h2>
<div class="tabs"><span class="on">Our Customers.</span><span class="off">Our Partners.</span></div>
<div class="partner" style="left:106px"><i></i>Norvik</div>
<div class="partner" style="left:282px">Orbelle</div>
<div class="partner" style="left:463px;font-size:26px">PLACEHOLDER</div>
<div class="partner" style="left:730px;font-size:27px"><i></i>Mailcrest</div>
<div class="partner" style="left:925px;font-size:17px;font-weight:500">BRIGHTVALE COMPANY</div>

<!-- CONTACT -->
<section class="contact" role="img" aria-label="Blue-tinted city skyline at night behind the contact area">
  <svg class="stripe" width="1200" height="563" viewBox="0 0 1200 563">
    <polygon points="78,0 130,0 0,175 0,105" fill="#33b8a4"/>
    <polygon points="1200,390 1200,462 1125,563 1040,563" fill="#33b8a4"/>
  </svg>
</section>
<div class="eyebrow" style="left:247px;top:3800px;color:#fff;font-size:15px">GET IN TOUCH</div>
<div class="abs" style="left:375px;top:3810px;width:122px;height:1px;background:rgba(255,255,255,.7)"></div>
<h2 class="abs" style="left:247px;top:3830px;font-size:44px;line-height:58px;font-weight:500;color:#fff">Let’s work<br>together</h2>
<div class="contact-row" style="top:3958px"><span class="ico"><svg width="13" height="13" viewBox="0 0 24 24"><path d="M6 3l3 0 2 5-2 1.5a12 12 0 0 0 5.5 5.5L16 13l5 2v3a2 2 0 0 1-2 2A16 16 0 0 1 4 5a2 2 0 0 1 2-2z" fill="#fff"/></svg></span><span style="padding-top:3px">(555) 014-2290</span></div>
<div class="contact-row" style="top:4004px"><span class="ico"><svg width="12" height="14" viewBox="0 0 12 16"><path d="M6 0a6 6 0 0 1 6 6c0 4-6 10-6 10S0 10 0 6a6 6 0 0 1 6-6z" fill="#fff"/><circle cx="6" cy="6" r="2" fill="#b868aa"/></svg></span><span>48 Larkfield Row<br>Easton 20419</span></div>
<div class="contact-row" style="top:4065px"><span class="ico"><svg width="13" height="10" viewBox="0 0 14 10"><rect width="14" height="10" fill="#fff"/><polyline points="0,0 7,6 14,0" fill="none" stroke="#b868aa" stroke-width="1.4"/></svg></span><span style="padding-top:3px">info@morvaneadvisory.com</span></div>
<div class="abs" style="left:292px;top:4114px;color:#fff;font-size:14.5px">Follow us</div>
<span class="social" style="left:244px"></span>
<span class="social" style="left:286px"></span>
<span class="social" style="left:330px"></span>
<span class="social" style="left:374px"></span>

<div class="form">
  <div class="form-head">We’d love to hear from you!</div>
  <div class="field" style="top:98px">Full Name</div>
  <div class="field" style="top:148px">Email</div>
  <div class="field" style="top:198px">Phone</div>
  <div class="field" style="top:248px;padding-bottom:34px">Message</div>
  <div class="btn" style="left:30px;top:321px;width:282px;height:42px">SUBMIT</div>
</div>

<!-- FOOTER -->
<footer class="footer">
  <div class="brand" style="left:109px;top:62px;font-size:30px"><span class="mark" style="width:22px;height:22px"></span>K7 Morvane</div>
  <span class="foot-link" style="left:445px">HOME</span>
  <span class="foot-link" style="left:577px">ABOUT US</span>
  <span class="foot-link" style="left:731px">SERVICES</span>
  <span class="foot-link" style="left:884px">BLOG</span>
  <span class="foot-link" style="left:999px">CONTACT US</span>
  <div class="abs" style="left:99px;top:141px;width:1002px;height:1px;background:rgba(255,255,255,.2)"></div>
  <div class="abs" style="left:0;top:164px;width:1200px;text-align:center;color:#fff;font-size:14px">© 2021 K7 Morvane Advisory Partners Ltd . All Rights Reserved.</div>
</footer>

</body>
</html>
```